Professional Home Buyer business card needed

I need a pretty straight forward business card designed. We help people that NEED to sell their homes solve problems. We perform all types of Real Estate transactions including flip, wholesale, investment, rental property and multi family. The card will mainly be used to give to prospective Sellers but will also be given to Real Estate Investors as well. It should professional and very easy to read, most clients are older people.

Target Market(s)

Distressed home sellers as well as Real Estate investors

Industry/Entity Type

Real Estate

Contact Information for Business Card

should be a professional layout

Colors
ec1f27
ffffff
000000

Requirements
Must have
• Large logo on back and smaller one on front. should utilize Red, white, and black.
• I am thinking of using a soft touch coating on the card so keep that in mind.
• Contact info should be very easy to read, think older clients.
Nice to have
• I would like to see a design with rounded corners on the card
Should not have
• pictures of homes or other home graphics.

```html
<!DOCTYPE html>
<html lang="en">
<head>
<meta charset="utf-8">
<title>Keystone Home Buyers – Business Card</title>
<link href="https://fonts.googleapis.com/css2?family=Roboto:wght@400;500;900&display=swap" rel="stylesheet">
<style>
  :root {
    --red: #ec1f27;
    --white: #ffffff;
    --black: #000000;
    --card-black: #161616;
    --stage: #232323;
    --ink-grey: #444444;
    --rule: #cfcfcf;
    --foil: #9a9a9a;
  }
  * { box-sizing: border-box; margin: 0; padding: 0; }
  html, body {
    width: 1200px; height: 800px; overflow: hidden;
    background: var(--stage);
    font-family: "Roboto", Arial, sans-serif;
  }
  .stage {
    width: 1200px; height: 800px;
    display: flex; flex-direction: column; align-items: center; justify-content: center;
    gap: 40px;
  }
  .card {
    width: 595px; height: 340px;
    border-radius: 8px;
    position: relative;
    overflow: hidden;
  }
  /* Back */
  .card--back {
    background: var(--card-black);
    display: flex; flex-direction: column; align-items: center; justify-content: center;
    gap: 14px;
  }
  .tagline {
    font-size: 13px; font-weight: 500; letter-spacing: 0.3em; text-transform: uppercase;
    white-space: nowrap;
  }
  .card--back .tagline { color: var(--foil); }
  .wordmark {
    display: flex; align-items: center; gap: 14px;
    font-weight: 900; text-transform: uppercase; line-height: 1;
    white-space: nowrap;
  }
  .wordmark__dot { border-radius: 50%; flex: none; }
  .card--back .wordmark { font-size: 34px; color: var(--foil); letter-spacing: 0.04em; }
  .card--back .wordmark__dot { width: 24px; height: 24px; background: var(--foil); }

  /* Front */
  .card--front {
    background: var(--white);
    display: flex; align-items: center;
    padding: 0 30px;
  }
  .front__brand {
    width: 252px; flex: none;
    display: flex; flex-direction: column; align-items: center; gap: 10px;
  }
  .card--front .tagline { color: var(--black); font-size: 9px; letter-spacing: 0.22em; }
  .card--front .wordmark { font-size: 16px; color: var(--black); letter-spacing: 0.02em; gap: 8px; }
  .card--front .wordmark__dot { width: 14px; height: 14px; background: var(--red); }
  .front__rule {
    width: 1px; height: 250px; background: var(--rule); margin: 0 22px 0 8px; flex: none;
  }
  .contact { flex: 1; min-width: 0; }
  .contact__name {
    color: var(--red); font-size: 21px; font-weight: 500; text-transform: uppercase; line-height: 1.1;
  }
  .contact__title {
    color: var(--black); font-size: 14px; font-weight: 500; text-transform: uppercase; margin-bottom: 14px;
  }
  .contact__address {
    font-style: normal; color: var(--ink-grey); font-size: 14px; line-height: 1.35; margin-bottom: 14px;
  }
  .contact__list { list-style: none; }
  .contact__item {
    display: flex; align-items: center; gap: 10px;
    color: var(--ink-grey); font-size: 14px; line-height: 1.55;
    white-space: nowrap;
  }
  .contact__icon { width: 13px; height: 13px; fill: var(--red); flex: none; }
</style>
</head>
<body>
<main class="stage">

  <section class="card card--back" aria-label="Card back">
    <p class="tagline">Fair offers, fast closings</p>
    <div class="wordmark"><span class="wordmark__dot"></span>Keystone Home Buyers</div>
  </section>

  <section class="card card--front" aria-label="Card front">
    <div class="front__brand">
      <p class="tagline">Fair offers, fast closings</p>
      <div class="wordmark"><span class="wordmark__dot"></span>Keystone Home Buyers</div>
    </div>
    <div class="front__rule"></div>
    <div class="contact">
      <h1 class="contact__name">Daniel Reyes</h1>
      <p class="contact__title">CEO/Founder</p>
      <address class="contact__address">4120 Birchwood Court<br>Anchorage, Alaska 99508</address>
      <ul class="contact__list">
        <li class="contact__item">
          <svg class="contact__icon" viewBox="0 0 16 16" aria-hidden="true"><path d="M3.6 1.2l2.3 2.6-1.3 2c.9 1.9 2.5 3.5 4.4 4.4l2-1.3 2.6 2.3-1.2 2.4C7.1 13.4 2.6 8.9 1.2 3.6z"/></svg>
          555 210 4417
        </li>
        <li class="contact__item">
          <svg class="contact__icon" viewBox="0 0 16 16" aria-hidden="true"><path d="M4 1h8v14H4zM5.5 3v9h5V3zM7 13h2v1H7z" fill-rule="evenodd"/></svg>
          555 386 9021
        </li>
        <li class="contact__item">
          <svg class="contact__icon" viewBox="0 0 16 16" aria-hidden="true"><path d="M4 1h8v4H4zM1 6h14v6h-3v3H4v-3H1zM5.5 10v3.5h5V10z" fill-rule="evenodd"/></svg>
          555 742 1603
        </li>
        <li class="contact__item">
          <svg class="contact__icon" viewBox="0 0 16 16" aria-hidden="true"><path d="M1 3h14v1.2L8 9 1 4.2zM1 5.8l7 4.8 7-4.8V13H1z"/></svg>
          daniel@keystonehomebuyers.com
        </li>
        <li class="contact__item">
          <svg class="contact__icon" viewBox="0 0 16 16" aria-hidden="true"><circle cx="8" cy="8" r="7"/></svg>
          www.keystonehomebuyers.com
        </li>
      </ul>
    </div>
  </section>

</main>
</body>
</html>
```